11 x 11 Flyer Design for Social Media - Reverse Mortgages

62 or older?

A Reverse Mortgage
could be
Your Road to Financial Freedom

* No Monthly Payments
* No Income Requirements
* No Credit Score Requirements
* No Loss of Ownership

Receive cash by lump sum, monthly installments or a line of credit!!

Call us today for a Free Consultation!!
(800) 471-2965

Bluegate Financial Services, Inc.
NMLS #318760
www.bluegatehome.com

```html
<!DOCTYPE html>
<html lang="en">
<head>
<meta charset="utf-8">
<title>Reverse Mortgage Flyer – Bluegate Financial Services, Inc.</title>
<link rel="stylesheet" href="https://fonts.googleapis.com/css2?family=Roboto:wght@400;700;900&display=swap">
<style>
  :root {
    --brand-blue: #0061a5;
    --accent-yellow: #fdf193;
    --top-rule: #fff59a;
    --bullet-green: #9ccb3b;
    --ink: #1f1f1f;
    --white: #ffffff;
    --logo-gold: #c9b776;
  }
  html, body {
    margin: 0;
    padding: 0;
    width: 1200px;
    height: 1200px;
    overflow: hidden;
    background: var(--white);
  }
  .flyer {
    display: block;
    width: 1200px;
    height: 1200px;
    font-family: "Roboto", Arial, sans-serif;
  }
  .company-name { font-weight: 700; font-size: 24px; letter-spacing: 2px; fill: var(--ink); }
  .company-meta { font-weight: 400; font-size: 24px; letter-spacing: 1.6px; fill: var(--ink); }
  .brand-mark-text { font-weight: 700; font-size: 24px; fill: var(--brand-blue); }
  .headline-yellow { font-weight: 900; fill: var(--accent-yellow); }
  .headline-white { font-weight: 900; fill: var(--white); }
  .kicker { font-weight: 700; fill: var(--white); }
  .benefit { font-weight: 400; font-size: 31px; fill: var(--white); }
  .payout-note { font-weight: 400; font-size: 27px; fill: var(--white); }
  .phone-number { font-weight: 700; fill: var(--accent-yellow); }
  .rule { stroke: var(--white); stroke-width: 1.6; }
</style>
</head>
<body>
<svg class="flyer" viewBox="0 0 1200 1200" xmlns="http://www.w3.org/2000/svg">
  <defs>
    <linearGradient id="portraitTone" x1="0" y1="0" x2="1" y2="1">
      <stop offset="0" stop-color="#8fd0cc"/>
      <stop offset="0.55" stop-color="#b9e2de"/>
      <stop offset="1" stop-color="#7d6a5c"/>
    </linearGradient>
  </defs>

  <!-- header -->
  <rect class="top-band" x="0" y="0" width="1200" height="6" fill="var(--top-rule)"/>
  <g class="brand-lockup">
    <circle cx="96" cy="96" r="22" fill="var(--logo-gold)"/>
    <text class="brand-mark-text" x="130" y="90">Bluegate Financial</text>
    <text class="brand-mark-text" x="130" y="120">Services, Inc.</text>
  </g>
  <g class="company-info">
    <text class="company-name" x="621" y="53">BLUEGATE FINANCIAL SERVICES, INC</text>
    <text class="company-meta" x="621" y="91">NMLS #318760</text>
    <text class="company-meta" x="621" y="129">www.bluegatehome.com</text>
  </g>

  <!-- blue body -->
  <rect class="body-panel" x="0" y="173" width="1200" height="1027" fill="var(--brand-blue)"/>
  <rect class="portrait" x="1" y="171" width="556" height="368" fill="url(#portraitTone)"
        role="img" aria-label="Photo of a thoughtful senior man resting his chin on his clasped hands"/>

  <!-- age question -->
  <text class="headline-yellow" x="624" y="360" font-size="170" textLength="188" lengthAdjust="spacingAndGlyphs">62</text>
  <text class="headline-white" x="623" y="481" font-size="95" textLength="476" lengthAdjust="spacingAndGlyphs">OR OLDER?</text>
  <line class="rule" x1="621" y1="539" x2="1146" y2="539"/>

  <!-- main message -->
  <text class="kicker" x="34" y="621" font-size="30" textLength="600" lengthAdjust="spacingAndGlyphs">A REVERSE MORTGAGE COULD BE YOUR ROAD TO</text>
  <line class="rule" x1="32" y1="638" x2="637" y2="638"/>
  <text class="headline-yellow" x="38" y="748" font-size="118" textLength="600" lengthAdjust="spacingAndGlyphs">FINANCIAL</text>
  <text class="headline-yellow" x="38" y="860" font-size="129" textLength="600" lengthAdjust="spacingAndGlyphs">FREEDOM</text>

  <!-- benefits -->
  <g class="benefit-list">
    <circle cx="700" cy="623" r="7" fill="var(--bullet-green)"/>
    <text class="benefit" x="737" y="634">No Monthly Payments</text>
    <circle cx="700" cy="660" r="7" fill="var(--bullet-green)"/>
    <text class="benefit" x="737" y="671">No Income Requirements</text>
    <circle cx="700" cy="698" r="7" fill="var(--bullet-green)"/>
    <text class="benefit" x="737" y="709">No Credit Score Requirements</text>
    <circle cx="700" cy="735" r="7" fill="var(--bullet-green)"/>
    <text class="benefit" x="737" y="746">No Loss of Ownership</text>
  </g>
  <text class="payout-note" x="694" y="826">Receive cash by lump sum, monthly</text>
  <text class="payout-note" x="694" y="859">installments or a line of credit!!</text>

  <line class="rule" x1="32" y1="887" x2="1148" y2="887"/>

  <!-- call to action -->
  <text class="headline-white" x="34" y="975" font-size="61" textLength="662" lengthAdjust="spacingAndGlyphs">CALL US TODAY FOR A</text>
  <text class="headline-yellow" x="38" y="1090" font-size="122" textLength="279" lengthAdjust="spacingAndGlyphs">FREE</text>
  <text class="headline-white" x="34" y="1168" font-size="61" textLength="497" lengthAdjust="spacingAndGlyphs">CONSULTATION!!</text>
  <text class="phone-number" x="618" y="1168" font-size="78" textLength="512" lengthAdjust="spacingAndGlyphs">(800)471-2965</text>
</svg>
</body>
</html>
```